Book Cover: A Quiet Cartographer

DO NOT JUST COPY THE BOOK COVER I HAVE ADDED FOR REFERENCE. I NEED SOMETHING FRESH NOT JUST A COPY AND PASTE!
If you cannot improve on the design with something creative then don't submit a design.

Project Title:
Book Cover Design for A Quiet Cartographer

Must be better than the mock design I have uploaded in project files.

Project Description:
I’m looking for a striking and emotionally evocative book cover for my upcoming title A Quiet Cartographer. This is a deeply personal and powerful memoir about the masks we wear, emotional survival, control, and the journey toward radical self-awareness and healing. The cover should visually represent the contrast between the performative self and the authentic self.

Visual Concept:
Please take visual inspiration and design continuity from my previous book Run FAR Now! — I will upload that cover for reference. This new design should feel like a continuation of the same author journey, but bolder and more psychologically intense.

You’ll be provided with two photos of me:

One where I appear more unkept, raw, and emotionally heavy.

One where I appear clean, centered, and lighter.

These can either be:

Split down the middle to create a “mirror” or duality effect (symbolizing the split self),

Or placed side by side as a subtle before/after or internal/external representation.

You may also consider overlaying or fading one into the other if done tastefully.

The mood should hint at internal conflict, self-reckoning, and healing—but without looking too “self-help cliché.” Think masculine, introspective, modern, and editorial. Avoid overly bright or busy visuals. A minimal or clean design with strong type hierarchy is preferred.

Key Themes to Represent Visually (even abstractly):

Narcissism as a survival mechanism

The emotional cost of performance

The tension between image and authenticity

The healing journey from ego to empathy

Design References:

Run FAR Now! (uploaded) — continuity of brand and typography encouraged

Memoir-style covers like Lanterns Along the Winter Harbour, Saltwater, or A Kettle Hums at Dusk for layout feel

If using color, muted tones with contrast (black/white, sepia, desaturated blues or greys) work well

Title: A Quiet Cartographer
Subtitle (optional placement): Not every narcissist is a monster. Some are just wounded men trying their best to survive
Author: Marlon Weskett

Deliverables:

Full front cover for print sale size as previous cover, including space for subtitle and author name

Spine and back cover (leave placeholder text if no blurb is given)

Ebook cover version

High-resolution files suitable for Quillmark QPS and print use

Additional Notes:
Please ensure the tone stays emotionally resonant, masculine, and sophisticated. No stock image models or cliché therapist symbols. Use my uploaded photos only.

Looking forward to seeing your vision come to life.

Back Cover Blurb – A Quiet Cartographer
A brutally honest recovery story—about what happens after you get clean, and the ego you still have to face.
Most people think addiction ends when you put down the drink, the drug, or the chaos.
But for Marlon Weskett, sobriety was just the start.
Behind the personal development posts, six-pack selfies, and billion-rand property deals, he was still chasing the one thing rehab never took from him: the need to be admired.
This book is not a confession. It’s a dismantling.
In A Quiet Cartographer, Marlon exposes the hidden patterns of ego, control, and validation-seeking that nearly cost him everything—even after he got “better.” With fearless self-inquiry and raw storytelling, he invites readers into his recovery from performance, perfectionism, and power addiction.
Whether you’ve been the narcissist—or you’ve loved one—this book is a mirror. And what you’ll find is not just insight, but a new path forward: one where truth is more powerful than charm, and safety matters more than being impressive.
This isn’t about being perfect.
It’s about being honest.
And finally becoming someone worth trusting—especially by yourself.

Target Market(s)

Any reader wanting to read about narcissism and love

Font styles to use
Sans Serif

Colors
EB3D1F
EC4F4E
F09395
F8D3D4
FCEDEE

Requirements
Must have
• Must be better than the mock design I uploaded.

```html
<!DOCTYPE html>
<html lang="en">
<head>
<meta charset="utf-8">
<title>A Quiet Cartographer — Marlon Weskett</title>
<link rel="stylesheet" href="https://fonts.googleapis.com/css2?family=Bebas+Neue&family=Oswald:wght@400;500;600&display=swap">
<style>
  :root {
    --ember: #eb3d1f;
    --coral: #ec4f4e;
    --rose: #f09395;
    --blush: #f8d3d4;
    --shell: #fcedee;
    --night: #121212;
    --band: #1b1b1b;
    --white: #ffffff;
  }
  * { margin: 0; padding: 0; box-sizing: border-box; }
  html, body { width: 901px; height: 1200px; overflow: hidden; background: var(--night); }
  .cover {
    position: relative;
    width: 901px;
    height: 1200px;
    overflow: hidden;
    background: var(--night);
  }
  .portrait-split {
    position: absolute;
    top: 0;
    left: 0;
    width: 901px;
    height: 860px;
  }
  .endorsement {
    position: absolute;
    top: 26px;
    left: 0;
    width: 100%;
    text-align: center;
    font-family: "Oswald", sans-serif;
    font-weight: 500;
    font-size: 20px;
    line-height: 26px;
    color: var(--shell);
  }
  .endorsement .endorser {
    color: var(--coral);
    text-transform: uppercase;
    letter-spacing: 1px;
  }
  .half-label {
    position: absolute;
    top: 660px;
    font-family: "Oswald", sans-serif;
    font-weight: 500;
    font-size: 15px;
    letter-spacing: 5px;
    text-transform: uppercase;
  }
  .half-label.mask { left: 60px; color: var(--rose); }
  .half-label.self { right: 60px; color: var(--blush); }
  .title {
    position: absolute;
    top: 730px;
    left: 0;
    width: 100%;
    text-align: center;
    font-family: "Bebas Neue", sans-serif;
    font-weight: 400;
    color: var(--white);
  }
  .title-lead {
    display: inline-block;
    background: var(--ember);
    padding: 6px 22px 0 40px;
    font-size: 76px;
    line-height: 72px;
    letter-spacing: 18px;
  }
  .title-main {
    display: block;
    font-size: 150px;
    line-height: 140px;
    letter-spacing: 2px;
    margin-top: 4px;
  }
  .title-rule {
    position: absolute;
    top: 964px;
    left: 410px;
    width: 81px;
    height: 4px;
    background: var(--ember);
  }
  .subtitle {
    position: absolute;
    top: 982px;
    left: 0;
    width: 100%;
    text-align: center;
    font-family: "Oswald", sans-serif;
  }
  .subtitle .hook {
    display: block;
    font-weight: 600;
    font-size: 30px;
    line-height: 38px;
    color: var(--coral);
  }
  .subtitle .rest {
    display: block;
    font-weight: 400;
    font-size: 21px;
    line-height: 30px;
    color: var(--blush);
  }
  .author-band {
    position: absolute;
    left: 0;
    bottom: 0;
    width: 100%;
    height: 112px;
    background: var(--band);
    border-top: 3px solid var(--ember);
    display: flex;
    align-items: center;
    justify-content: center;
  }
  .author {
    font-family: "Bebas Neue", sans-serif;
    font-size: 68px;
    letter-spacing: 16px;
    padding-left: 16px;
    padding-top: 6px;
    color: var(--white);
  }
</style>
</head>
<body>
<main class="cover">
  <svg class="portrait-split" viewBox="0 0 901 860">
    <defs>
      <linearGradient id="raw-half" x1="0" y1="0" x2="1" y2="1">
        <stop offset="0" stop-color="#2a2a2b"/>
        <stop offset="0.45" stop-color="#55504e"/>
        <stop offset="0.8" stop-color="#302d2c"/>
        <stop offset="1" stop-color="#161616"/>
      </linearGradient>
      <linearGradient id="clear-half" x1="1" y1="0" x2="0" y2="1">
        <stop offset="0" stop-color="#d9c3b8"/>
        <stop offset="0.45" stop-color="#c29a88"/>
        <stop offset="0.8" stop-color="#8e6d60"/>
        <stop offset="1" stop-color="#3a2f2b"/>
      </linearGradient>
      <linearGradient id="floor-fade" x1="0" y1="0" x2="0" y2="1">
        <stop offset="0" stop-color="#121212" stop-opacity="0"/>
        <stop offset="1" stop-color="#121212" stop-opacity="1"/>
      </linearGradient>
      <linearGradient id="head-fade" x1="0" y1="0" x2="0" y2="1">
        <stop offset="0" stop-color="#121212" stop-opacity="0.9"/>
        <stop offset="1" stop-color="#121212" stop-opacity="0"/>
      </linearGradient>
    </defs>
    <rect role="img" aria-label="Author photo, left half of the face: unkept, bearded, heavy, desaturated" x="0" y="0" width="452" height="860" fill="url(#raw-half)"/>
    <rect role="img" aria-label="Author photo, right half of the face: clean shaven, calm, lighter, warm tone" x="449" y="0" width="452" height="860" fill="url(#clear-half)"/>
    <rect x="0" y="0" width="901" height="170" fill="url(#head-fade)"/>
    <rect x="0" y="540" width="901" height="320" fill="url(#floor-fade)"/>
    <polyline class="fault-line" fill="none" stroke="#eb3d1f" stroke-width="5" stroke-linejoin="miter"
      points="450,110 462,170 441,230 458,290 444,350 463,410 439,470 456,530 446,590 452,650"/>
    <g class="survey-ticks" stroke="#f09395" stroke-width="2">
      <line x1="472" y1="200" x2="492" y2="200"/>
      <line x1="408" y1="320" x2="428" y2="320"/>
      <line x1="474" y1="440" x2="494" y2="440"/>
      <line x1="410" y1="560" x2="430" y2="560"/>
    </g>
  </svg>

  <p class="endorsement">“Whatever we’ve been through, Marlon not only makes us feel we can<br>get over it, he gives us the tools to do exactly that.” <span class="endorser">— Adrian Kessler</span></p>

  <span class="half-label mask">The performance</span>
  <span class="half-label self">The person</span>

  <h1 class="title">
    <span class="title-lead">A Quiet</span>
    <span class="title-main">Cartographer</span>
  </h1>

  <span class="title-rule"></span>

  <p class="subtitle">
    <span class="hook">Not every narcissist is a monster.</span>
    <span class="rest">Some are just wounded men trying their best to survive</span>
  </p>

  <footer class="author-band">
    <p class="author">MARLON WESKETT</p>
  </footer>
</main>
</body>
</html>
```